lunch and dinne(al a carte) menus

we are a medium sized licenced club that has taken back the dining in the club
in the western suburbs of sydney working class with a rugby league base
our logo is a wolf kelford hawks

Reason: We have changed the name to Bluegate grill it could be done as Bluegate or Bluegate or Bluegate We need a lunch menu and a seperate dinner menu eg Bluegate grill l u n c h or Bluegate grill d i n n e r

Reason: Weve changed the name

Target Market(s)

young families, working class rugby leagues sporty types

Industry/Entity Type

Club

Requirements
Must have
• user friendly

```html
<!DOCTYPE html>
<html lang="en">
<head>
<meta charset="utf-8">
<title>Bluegate Grill – Lunch and Dinner Menu Covers</title>
<link rel="stylesheet" href="https://fonts.googleapis.com/css2?family=Open+Sans:wght@400&display=swap">
<style>
  :root {
    --paper: #ffffff;
    --ink: #1e1e1e;
    --teal-deep: #136e7e;
    --teal-soft: #4f9c96;
    --lime: #a8cd3e;
    --mint: #84cda7;
    --mint-pale: #9fd7a8;
    --leaf: #a9cf8f;
    --orange: #f05a2a;
    --tan: #c79a66;
    --card-light: #f6f3f0;
    --card-shade: #d8cfca;
  }
  * { box-sizing: border-box; margin: 0; padding: 0; }
  html, body { width: 849px; height: 1200px; overflow: hidden; background: var(--paper); }
  body { position: relative; font-family: "Open Sans", Arial, sans-serif; color: var(--ink); }

  .menu-cover {
    position: absolute; left: 96px; width: 694px; height: 447px;
    display: flex; gap: 5px;
  }
  .menu-cover--lunch { top: 93px; }
  .menu-cover--dinner { top: 580px; }

  .cover-front { position: relative; width: 343px; height: 100%; }
  .front-stripes {
    position: absolute; inset: 0 0 113px 0;
    background: linear-gradient(90deg,
      var(--teal-deep) 0 40px, var(--lime) 40px 74px, var(--mint) 74px 128px,
      var(--orange) 128px 193px, var(--teal-deep) 193px 266px, var(--mint) 266px 292px,
      var(--orange) 292px 343px);
  }
  .cutlery-art {
    position: absolute; left: 48px; top: 28px; width: 222px; height: 236px;
    background: linear-gradient(180deg, var(--card-light), var(--card-shade));
  }
  .front-band {
    position: absolute; left: 0; right: 0; bottom: 0; height: 113px;
    background: var(--mint);
    display: flex; align-items: center; gap: 10px; padding-left: 24px;
    font-size: 24px; font-weight: 400; color: var(--ink);
  }
  .venue-dot { width: 14px; height: 14px; border-radius: 50%; background: var(--ink); }

  .cover-back {
    position: relative; flex: 1; height: 100%;
    background: linear-gradient(90deg,
      var(--teal-soft) 0 37px, var(--mint-pale) 37px 57px, var(--leaf) 57px 99px,
      var(--mint-pale) 99px 128px, var(--tan) 128px 193px, var(--teal-soft) 193px 258px,
      var(--mint-pale) 258px 292px, var(--tan) 292px 345px);
  }
  .menu-title {
    position: absolute; left: 82px; top: 40px;
    font-size: 21px; font-weight: 400; letter-spacing: 0.3px; color: var(--ink);
    white-space: nowrap;
  }

  .brief-note {
    position: absolute; left: 0; right: 0; top: 1118px;
    text-align: center; font-size: 21px; color: var(--ink);
  }
</style>
</head>
<body>

<section class="menu-cover menu-cover--lunch">
  <div class="cover-front">
    <div class="front-stripes"></div>
    <div class="cutlery-art" role="img" aria-label="Illustration of fork, knife and spoon on white cards"></div>
    <div class="front-band"><span class="venue-dot"></span><span class="venue-name">Bluegate Grill</span></div>
  </div>
  <div class="cover-back">
    <h2 class="menu-title">LUNCH MENU</h2>
  </div>
</section>

<section class="menu-cover menu-cover--dinner">
  <div class="cover-front">
    <div class="front-stripes"></div>
    <div class="cutlery-art" role="img" aria-label="Illustration of fork, knife and spoon on white cards"></div>
    <div class="front-band"><span class="venue-dot"></span><span class="venue-name">Bluegate Grill</span></div>
  </div>
  <div class="cover-back">
    <h2 class="menu-title">DINNER MENU</h2>
  </div>
</section>

<p class="brief-note">Send me a text menu (Word document, etc)</p>

</body>
</html>
```